The Lantern and the Meadow: Songs Of Quiet Bloom

We need a book cover/spine and back cover for a multi author book called the Lantern and The Meadow: Songs of Quiet Bloom. This will be a collection of stories from women who major transformational stories to tell. They embark on a voyage, find themselves in uncharted territory, find friends or allies and in the end find themselves back home to themselves. I want this book cover to feel fun of wonder, adventure, intrigue with a a dainty energy. I have uploaded some images for inspiration but not to use in the design because they are not images I have permission to use.

```html
<!DOCTYPE html>
<html lang="en">
<head>
<meta charset="utf-8">
<title>The Lantern and the Meadow: Songs Of Quiet Bloom — Cover Wrap</title>
<link href="https://fonts.googleapis.com/css2?family=Allura&family=EB+Garamond:wght@400&family=Jost:wght@300;400&family=Mulish:wght@400&display=swap" rel="stylesheet">
<style>
  :root {
    --page-bg: #ffffff;
    --sky-dusk: #6e5a55;
    --sky-glow: #f3e3c2;
    --gold: #d9a456;
    --amber: #c27a3a;
    --poppy: #b8321f;
    --poppy-deep: #7e1c15;
    --spine-gold: #b8843f;
    --spine-ink: #3a1c10;
    --maroon: #5a1a2a;
    --author-gold: #f3c979;
    --ink: #1e1412;
    --white: #ffffff;
    --panel-veil: rgba(255, 240, 230, 0.26);
  }
  * { box-sizing: border-box; margin: 0; padding: 0; }
  html, body {
    width: 1200px; height: 1200px; overflow: hidden;
    background: var(--page-bg);
  }
  .wrap {
    position: absolute; left: 40px; top: 200px;
    width: 1120px; height: 799px;
    display: flex;
  }
  .back, .front { position: relative; width: 535.5px; height: 100%; overflow: hidden; }
  .spine {
    position: relative; width: 49px; height: 100%;
    background: linear-gradient(180deg, var(--spine-gold), #c99050 55%, #9c5a2c);
  }
  .scene {
    position: absolute; inset: 0;
    background:
      radial-gradient(ellipse 60% 35% at 55% 40%, rgba(255,248,228,0.9), rgba(255,248,228,0) 70%),
      linear-gradient(180deg, var(--sky-dusk) 0%, #a78a6e 18%, var(--sky-glow) 38%, var(--gold) 58%, var(--amber) 68%, var(--poppy) 82%, var(--poppy-deep) 100%);
  }
  .back .scene {
    background:
      radial-gradient(ellipse 70% 30% at 60% 28%, rgba(255,240,210,0.8), rgba(255,240,210,0) 70%),
      linear-gradient(180deg, #7a5a48 0%, #c79a6a 20%, #e9c089 40%, #d79457 62%, var(--poppy) 82%, var(--poppy-deep) 100%);
  }
  .title {
    position: absolute; left: 0; right: 0; text-align: center;
    font-family: "Allura", cursive; color: var(--white);
    line-height: 0.9; font-weight: 400;
    text-shadow: 0 2px 10px rgba(60,30,20,0.35);
  }
  .title .second { display: block; padding-left: 0.1em; }
  .subtitle {
    position: absolute; left: 0; right: 0; text-align: center;
    font-family: "Jost", sans-serif; font-weight: 300; color: var(--maroon);
  }
  .back .title { top: 36px; font-size: 50px; }
  .back .subtitle { top: 146px; font-size: 17px; }
  .blurb {
    position: absolute; left: 40px; top: 190px; width: 463px; height: 433px;
    background: var(--panel-veil);
    padding: 34px 26px 0;
    font-family: "Mulish", sans-serif; font-size: 11.6px; line-height: 16.3px;
    color: var(--ink); text-align: center;
  }
  .blurb p + p { margin-top: 16px; }
  .code-box {
    position: absolute; left: 335px; top: 672px; width: 178px; height: 106px;
    background: var(--white);
  }
  .spine-text {
    position: absolute; top: 22px; left: 50%;
    writing-mode: vertical-rl;
    font-family: "Jost", sans-serif; font-weight: 300; color: var(--spine-ink);
    white-space: nowrap;
  }
  .spine-title { transform: translateX(-62%); font-size: 14.5px; letter-spacing: 0.2px; }
  .spine-authors {
    position: absolute; top: 500px; left: 50%; transform: translateX(-40%);
    writing-mode: vertical-rl; font-family: "Jost", sans-serif; font-weight: 300;
    font-size: 13.5px; line-height: 17px; color: var(--spine-ink); white-space: nowrap;
  }
  .front .title { top: 20px; font-size: 92px; }
  .front .subtitle { top: 210px; font-size: 28px; }
  .authors {
    position: absolute; left: 0; right: 18px; top: 680px; text-align: right;
    font-family: "Jost", sans-serif; font-weight: 300; color: var(--author-gold);
    font-size: 23.5px; line-height: 30px;
  }
  .publisher {
    position: absolute; right: 38px; top: 756px;
    font-family: "EB Garamond", serif; font-size: 18px; color: var(--white);
  }
</style>
</head>
<body>
  <main class="wrap">
    <section class="back">
      <div class="scene" role="img" aria-label="Soft-focus field of red poppies under a golden sunset sky"></div>
      <h2 class="title">The Lantern and<span class="second">the Meadow:</span></h2>
      <p class="subtitle">Songs Of Quiet Bloom</p>
      <div class="blurb">
        <p>Lorem ipsum dolor sit amet, consectetur adipiscing elit, sed do eiusmod tempor incididunt ut labore et dolore magna aliqua. Ut enim ad minim veniam, quis nostrud exercitation ullamco laboris nisi ut aliquip ex ea commodo consequat. Duis aute irure dolor in reprehenderit in voluptate velit esse cillum dolore eu fugiat nulla pariatur. Excepteur sint occaecat cupidatat non proident, sunt in culpa qui officia deserunt mollit anim id est laborum.</p>
        <p>Sed ut perspiciatis unde omnis iste natus error sit voluptatem accusantium doloremque laudantium, totam rem aperiam, eaque ipsa quae ab illo inventore veritatis et quasi architecto beatae vitae dicta sunt explicabo. Nemo enim ipsam voluptatem quia voluptas sit aspernatur aut odit aut fugit, sed quia consequuntur magni dolores eos qui ratione voluptatem sequi nesciunt. Neque porro quisquam est, qui dolorem ipsum quia dolor sit amet, consectetur, adipisci velit, sed quia non numquam eius modi tempora incidunt ut labore et dolore magnam aliquam quaerat voluptatem. Ut enim ad minima veniam, quis nostrum exercitationem ullam corporis suscipit laboriosam, nisi ut aliquid ex ea commodi consequatur? Quis autem vel eum iure reprehenderit qui in ea voluptate velit esse quam nihil molestiae consequatur, vel illum qui dolorem eum fugiat quo voluptas nulla pariatur?</p>
      </div>
      <div class="code-box"></div>
    </section>

    <section class="spine">
      <p class="spine-text spine-title">THE LANTERN AND THE MEADOW - Songs Of Quiet Bloom</p>
      <p class="spine-authors">Author Name - Author Name - Author Name<br>Author Name - Author Name - Author Name</p>
    </section>

    <section class="front">
      <div class="scene" role="img" aria-label="Woman in a flowing red gown standing in a poppy meadow, arm outstretched toward a glowing sunset sky"></div>
      <h1 class="title">The Lantern and<span class="second">the Meadow:</span></h1>
      <p class="subtitle">Songs Of Quiet Bloom</p>
      <p class="authors">Author Name - Author Name - Author Name<br>Author Name - Author Name - Author Name</p>
      <p class="publisher">Gentle Harbor Press</p>
    </section>
  </main>
</body>
</html>
```